" Já sou fotógrafo e possuo uma marca chamada Otávio Rangel, mais voltada para casamentos, ensaios de casais e família. Todavia já realizei muitos trabalhos no mundo corporativo, como vídeos institucionais de empresas, fotografia gastronômica, foto de carros e vídeos, foto de lojas e estabelecimentos comerciais. Daí que criei a Tulco produções para ser a empresa que irá divulgar esse tipo de material e vender por ela tais produtos de foto e filme. E por ser produções, não se ter;a um limite, poderá oferecer projetos para mídias sociais, campanhas publicitárias e afins. "

```html
<!DOCTYPE html>
<html lang="pt-BR">
<head>
<meta charset="utf-8">
<title>Tulco Produções — cartões de visita</title>
<link rel="stylesheet" href="https://fonts.googleapis.com/css2?family=Raleway:wght@300;400&display=swap">
<style>
  :root {
    --bg: #262626;
    --card-top: #2e2e30;
    --card-bottom: #1c1c1e;
    --card-edge: #3a3a3c;
    --brand-green: #49e01e;
    --text-light: #e6e6e6;
    --text-muted: #9a9a9a;
    --icon-fill: #5a5a5c;
    --icon-glyph: #1e1e20;
  }
  * { box-sizing: border-box; margin: 0; padding: 0; }
  html, body { width: 1200px; height: 1200px; overflow: hidden; background: var(--bg); }
  body { position: relative; font-family: "Raleway", sans-serif; }

  .card {
    position: absolute;
    top: 240px;
    width: 422px;
    height: 720px;
    border-radius: 26px;
    background: linear-gradient(160deg, var(--card-top), var(--card-bottom));
    border: 1px solid var(--card-edge);
    box-shadow: 0 10px 30px rgba(0,0,0,.45);
  }
  .card--front { left: 150px; }
  .card--back { left: 604px; }

  .wordmark {
    position: absolute;
    left: 0; right: 0;
    display: flex;
    align-items: center;
    justify-content: center;
    gap: 18px;
  }
  .card--front .wordmark { top: 340px; }
  .card--back .wordmark { top: 140px; }
  .wordmark__dot {
    width: 26px; height: 26px; border-radius: 50%;
    background: var(--brand-green);
  }
  .wordmark__name {
    color: var(--text-light);
    font-weight: 300;
    font-size: 56px;
    letter-spacing: 6px;
    line-height: 1;
    text-transform: uppercase;
  }
  .wordmark__name small {
    display: block;
    font-size: 15px;
    letter-spacing: 10px;
    margin-top: 10px;
    text-align: center;
  }

  .contact-list { list-style: none; position: absolute; inset: 0; }
  .contact-item {
    position: absolute;
    display: flex;
    align-items: center;
    gap: 14px;
    color: var(--text-muted);
    font-size: 11px;
    letter-spacing: .5px;
    line-height: 1.5;
    text-transform: uppercase;
  }
  .contact-item svg { flex: none; width: 30px; height: 30px; }
  .contact-item--email { left: 190px; top: 388px; }
  .contact-item--phone { left: 150px; top: 441px; }
  .contact-item--address { left: 112px; top: 503px; }
  .contact-item--web { left: 72px; top: 556px; }
</style>
</head>
<body>
  <section class="card card--front" aria-label="Frente do cartão">
    <div class="wordmark">
      <span class="wordmark__dot"></span>
      <p class="wordmark__name">Tulco<small>Produções</small></p>
    </div>
  </section>

  <section class="card card--back" aria-label="Verso do cartão">
    <div class="wordmark">
      <span class="wordmark__dot"></span>
      <p class="wordmark__name">Tulco<small>Produções</small></p>
    </div>

    <ul class="contact-list">
      <li class="contact-item contact-item--email">
        <svg viewBox="0 0 30 30" aria-hidden="true"><circle cx="15" cy="15" r="15" fill="var(--icon-fill)"/><rect x="8" y="10" width="14" height="10" rx="1" fill="var(--icon-glyph)"/><path d="M8 10.5 15 16l7-5.5" stroke="var(--icon-fill)" stroke-width="1.2" fill="none"/></svg>
        <span>contato@tulcofilmes.com</span>
      </li>
      <li class="contact-item contact-item--phone">
        <svg viewBox="0 0 30 30" aria-hidden="true"><circle cx="15" cy="15" r="15" fill="var(--icon-fill)"/><path d="M11 8h3l1.2 3.5-1.8 1.3a8 8 0 0 0 3.8 3.8l1.3-1.8L22 16v3a2 2 0 0 1-2 2A11 11 0 0 1 9 10a2 2 0 0 1 2-2z" fill="var(--icon-glyph)"/></svg>
        <span>+55 21 3456 7801<br>+55 21 9876 5402</span>
      </li>
      <li class="contact-item contact-item--address">
        <svg viewBox="0 0 30 30" aria-hidden="true"><circle cx="15" cy="15" r="15" fill="var(--icon-fill)"/><path d="M15 7 7 14h2.5v8h4v-5h3v5h4v-8H23z" fill="var(--icon-glyph)"/></svg>
        <span>Rua das Palmeiras, 210<br>Rio de Janeiro, Brasil</span>
      </li>
      <li class="contact-item contact-item--web">
        <svg viewBox="0 0 30 30" aria-hidden="true"><circle cx="15" cy="15" r="15" fill="var(--icon-fill)"/><circle cx="15" cy="15" r="7.5" fill="none" stroke="var(--icon-glyph)" stroke-width="1.6"/><ellipse cx="15" cy="15" rx="3.2" ry="7.5" fill="none" stroke="var(--icon-glyph)" stroke-width="1.4"/><path d="M7.5 15h15" stroke="var(--icon-glyph)" stroke-width="1.4"/></svg>
        <span>www.tulcofilmes.com</span>
      </li>
    </ul>
  </section>
</body>
</html>
```